Building Company Business Card Design

I am looking to get a business card designed for my Building Company. Please find the logo attached.

Industry/Entity Type

Business

Contact Information for Business Card

Mobile 0472 913 046
Email admin@tarrowconstructworks.com.au
Website www.tarrowconstructworks.com.au

Colors
0255a3

```html
<!DOCTYPE html>
<html lang="en">
<head>
<meta charset="utf-8">
<title>Tarrow Construct Works – Business Card</title>
<link rel="stylesheet" href="https://fonts.googleapis.com/css2?family=Open+Sans:wght@400;600&display=swap">
<style>
  :root {
    --brand-blue: #0255a3;
    --link-blue: #2a4fa8;
    --ink: #111111;
    --card-white: #f4f4f4;
    --card-black: #141414;
    --backdrop: #2b2b2b;
  }
  * { margin: 0; padding: 0; box-sizing: border-box; }
  html, body {
    width: 1200px;
    height: 600px;
    overflow: hidden;
    background: var(--backdrop);
    font-family: "Open Sans", Arial, sans-serif;
  }
  .canvas {
    position: relative;
    width: 1200px;
    height: 600px;
  }
  .card {
    position: absolute;
    top: 160px;
    width: 500px;
    height: 290px;
    border-radius: 18px;
  }
  .card--front { left: 75px; background: var(--card-white); }
  .card--back { left: 625px; background: var(--card-black); }

  .wordmark {
    color: var(--brand-blue);
    font-weight: 600;
    font-size: 22px;
    letter-spacing: 0.5px;
    text-transform: uppercase;
    white-space: nowrap;
  }
  .website {
    color: var(--link-blue);
    font-size: 12.5px;
    font-weight: 400;
  }

  .front-brand {
    position: absolute;
    top: 40px;
    right: 30px;
    text-align: right;
  }
  .front-brand .website { margin-top: 6px; display: block; }

  .identity {
    position: absolute;
    left: 32px;
    top: 186px;
  }
  .identity__name {
    color: var(--ink);
    font-size: 20px;
    font-weight: 400;
    line-height: 1.2;
  }
  .identity__title {
    color: var(--link-blue);
    font-size: 12px;
    margin-top: 2px;
  }
  .divider {
    position: absolute;
    left: 32px;
    right: 30px;
    top: 236px;
    height: 3px;
    background: var(--brand-blue);
  }
  .contact {
    position: absolute;
    left: 32px;
    right: 30px;
    top: 248px;
    display: flex;
    justify-content: space-between;
    align-items: center;
    font-size: 13.5px;
    color: var(--ink);
  }
  .contact__item { display: flex; align-items: center; gap: 6px; }
  .contact__icon { width: 14px; height: 14px; fill: var(--brand-blue); }

  .back-brand {
    position: absolute;
    left: 0;
    right: 0;
    top: 128px;
    text-align: center;
  }
  .back-brand .wordmark { font-size: 24px; color: var(--brand-blue); }
  .back-brand .website { display: block; margin-top: 48px; font-size: 11.5px; }
</style>
</head>
<body>
<main class="canvas">
  <section class="card card--front">
    <div class="front-brand">
      <div class="wordmark">Tarrow Construct Works</div>
      <span class="website">www.tarrowconstructworks.com.au</span>
    </div>

    <div class="identity">
      <div class="identity__name">Your Name</div>
      <div class="identity__title">Job Title</div>
    </div>

    <div class="divider"></div>

    <div class="contact">
      <span class="contact__item">
        <svg class="contact__icon" viewBox="0 0 16 16" aria-hidden="true">
          <path d="M1 5c0-2 3-3 7-3s7 1 7 3v1.5h-3.5V5h-7v1.5H1z"/>
          <path d="M4 7h8l2 6H2z"/>
        </svg>
        0472 913 046
      </span>
      <span class="contact__item">
        admin@tarrowconstructworks.com.au
        <svg class="contact__icon" viewBox="0 0 16 16" aria-hidden="true">
          <path d="M1 3h14v10H1z" />
          <path d="M1 3l7 5.5L15 3" fill="none" stroke="#f4f4f4" stroke-width="1.2"/>
        </svg>
      </span>
    </div>
  </section>

  <section class="card card--back">
    <div class="back-brand">
      <div class="wordmark">Tarrow Construct Works</div>
      <span class="website">www.tarrowconstructworks.com.au</span>
    </div>
  </section>
</main>
</body>
</html>
```